Letterhead, envelope & business card design

We would like to refresh the look and feel of our business cards & letterheads.

Our company specialises in premium property.

We are looking for a unique minimalist design for our letterhead & business cards that project this.

I can send over examples of our current design to draw from, although Im looking for some one with creativity, yet focussed on a clean modern, minimalist design.
Updates

I have just uploaded our current letterhead.

We have just removed the 'swoosh' grey symbol, but would still like to keep some part of grey in the design if possible.

thanks in advance.

Just uploaded my details for business card.

Can we see examples with the light grey used as the secondary color?

thanks in advance.

Target Market(s)

We are a premium real estate agency & we want that message to be carried through our business cards & stationery.

Industry/Entity Type

Business

```html
<!DOCTYPE html>
<html lang="en">
<head>
<meta charset="utf-8">
<title>Harlow Estate Agents – Business Card</title>
<link href="https://fonts.googleapis.com/css2?family=Questrial&family=Roboto+Condensed:ital,wght@0,400;0,700;1,400&display=swap" rel="stylesheet">
<style>
  :root {
    --backdrop: #8fa4b3;
    --card: #ffffff;
    --navy: #1b3461;
    --blue: #2b5ca8;
    --text-grey: #5a5a5a;
    --bar-grey: #6e6e6e;
    --brand-grey: #a8bac4;
  }
  * { margin: 0; padding: 0; box-sizing: border-box; }
  html, body { width: 1200px; height: 848px; overflow: hidden; }
  body {
    background: var(--backdrop);
    position: relative;
    font-family: "Roboto Condensed", "Arial Narrow", sans-serif;
    color: var(--text-grey);
  }
  .card {
    position: absolute;
    top: 267px;
    width: 484px;
    height: 295px;
    background: var(--card);
  }
  .card--front { left: 96px; }
  .card--back { left: 620px; }

  .accent-bar {
    position: absolute;
    top: 0;
    height: 11px;
    background: var(--bar-grey);
  }
  .card--front .accent-bar { left: 184px; right: 2px; }
  .card--back .accent-bar { left: 0; width: 297px; }

  .brand {
    position: absolute;
    top: 22px;
    font-family: "Roboto Condensed", "Arial Narrow", sans-serif;
    font-weight: 400;
    font-size: 17px;
    letter-spacing: 1.5px;
    text-transform: uppercase;
    color: var(--brand-grey);
    line-height: 1;
  }
  .card--front .brand { left: 33px; }
  .card--back .brand { right: 26px; }

  .holder {
    position: absolute;
    right: 32px;
    top: 82px;
    text-align: right;
  }
  .holder__name {
    font-family: "Questrial", sans-serif;
    font-size: 37px;
    color: var(--navy);
    line-height: 1.05;
    letter-spacing: 0.5px;
  }
  .holder__role {
    font-style: italic;
    font-size: 20px;
    color: var(--text-grey);
    line-height: 1;
  }

  .website {
    position: absolute;
    right: 26px;
    top: 144px;
    font-size: 19px;
    font-weight: 400;
    color: var(--navy);
  }

  .contact-list {
    position: absolute;
    list-style: none;
    font-size: 17px;
    line-height: 23px;
  }
  .contact-list li { white-space: nowrap; }
  .label {
    display: inline-block;
    width: 18px;
    font-weight: 700;
    color: var(--blue);
  }
  .pin {
    display: inline-block;
    width: 18px;
    vertical-align: -2px;
  }
  .pin svg { width: 10px; height: 14px; fill: var(--navy); }

  .card--front .contact-list--phones { left: 36px; top: 203px; }
  .card--front .contact-list--office { left: 212px; top: 219px; font-size: 16.5px; line-height: 25px; }
  .card--back .contact-list--phones { left: 34px; top: 192px; }
  .card--back .contact-list--office { left: 216px; top: 214px; font-size: 16.5px; line-height: 25px; }

  .registration {
    font-size: 15px;
    color: var(--blue);
    margin-top: 3px;
  }
  .registration__number { color: var(--text-grey); }
</style>
</head>
<body>

  <section class="card card--front" aria-label="Business card front">
    <div class="accent-bar"></div>
    <div class="brand">Harlow Estate Agents</div>

    <div class="holder">
      <div class="holder__name">Evan Harlow</div>
      <div class="holder__role">director</div>
    </div>

    <ul class="contact-list contact-list--phones">
      <li><span class="label">M</span>0400 555 123</li>
      <li><span class="label">T</span>02 5550 1200</li>
      <li><span class="label">F</span>02 5550 1201</li>
    </ul>

    <ul class="contact-list contact-list--office">
      <li><span class="label">E</span>info@harlowestates.com.au</li>
      <li><span class="pin"><svg viewBox="0 0 10 14" aria-hidden="true"><path d="M5 0C2.2 0 0 2.2 0 5c0 3.5 5 9 5 9s5-5.5 5-9C10 2.2 7.8 0 5 0zm0 7a2 2 0 1 1 0-4 2 2 0 0 1 0 4z"/></svg></span>18 Ridge Street, Elmwood NSW 2000</li>
    </ul>
  </section>

  <section class="card card--back" aria-label="Business card back">
    <div class="accent-bar"></div>
    <div class="brand">Harlow Estate Agents</div>

    <div class="website">www.harlowestates.com.au</div>

    <ul class="contact-list contact-list--phones">
      <li><span class="label">T</span>02 5550 1200</li>
      <li><span class="label">F</span>02 5550 1201</li>
      <li class="registration">Registered Valuer <span class="registration__number">000 123</span></li>
    </ul>

    <ul class="contact-list contact-list--office">
      <li><span class="pin"><svg viewBox="0 0 10 14" aria-hidden="true"><path d="M5 0C2.2 0 0 2.2 0 5c0 3.5 5 9 5 9s5-5.5 5-9C10 2.2 7.8 0 5 0zm0 7a2 2 0 1 1 0-4 2 2 0 0 1 0 4z"/></svg></span>18 Ridge Street, Elmwood NSW 2000</li>
      <li><span class="label">E</span>info@harlowestates.com.au</li>
    </ul>
  </section>

</body>
</html>
```